Kunststoffverpackung für Falkor Snacks
Zielgruppe
Wir sind ein kleines Unternehmen, welches Bisonfleisch aus Nordamerika importiert und vertreibt. Unser neustes Produkt sind Falkor Snacks, deren Verpackung wir uns gerne designen lassen möchten.
Aufgabenstellung:
Design Entwurf für eine Kunststoffverpackung für Falkor Snacks (Trockenfleisch), von kanadischem Bison.
Preissegment: hochpreisig
Verkauf: Delikatessengeschäfte, hochpreisige Kaufhäuser (zb Lumhaus Berlin)
Design: edel, understatement, wenige ausgewählte Farben
Implizierte Message: hochwertiges, nachhaltiges Produkt für Feinschmecker und gesundheitsbewusste Sportler/Abenteurer.
USP: Jerky aus original kanadischem Bisonfleisch, artgerecht aufgezogen, ohne Medikamente, Wachstumshormone oder Futterzusätze
Besondere Produkteigenschaft: Kein Zucker, hoher Proteinanteil, hoher Eisenanteil, niedriger Cholesterinwert, kaum Fett, wenig Salz.
Aufgabenstellung
Zusätzliche Infos zu unserem Bisonfleisch findest du hier:
https://weidekorn-example.de/blogs/news/uber-uns-bisonfleisch-das-beste-fleisch-der-welt
https://weidekorn-example.de/blogs/news/bison-steak-guide
Zusätzliche Informationen zu Bisons findest du hier:
https://weidekorn-example.de/pages/bison-wiki
Auf der Rückseite bitte Platz lassen für folgende Grafiken/Informationen, daher bitte Platzhalter einfügen:
- Zutatenliste
- Nährwerttabelle
- Strichcode
- Recyclinglabel
Maße für die Verpackung sind:
170mm Länge
130mm Breite
Fotos wie die Verpackung auf keinen Fall aussehen sollen befinden sich mit dem Namen 'Dont' anbei. Verpackungen die uns vom Design gefallen befinden sich mit dem Namen 'Do' anbei.
Bei Rückfragen bitte mobil oder per mail wenden an:
Matthias Oldörp

```html
<!DOCTYPE html>
<html lang="de">
<head>
<meta charset="utf-8">
<title>Trockenfleisch-Verpackung – Rückseite</title>
<link href="https://fonts.googleapis.com/css2?family=Black+Ops+One&family=PT+Sans:wght@400&family=PT+Sans+Narrow:wght@400&display=swap" rel="stylesheet">
<style>
  :root{
    --page:#ffffff;
    --sky:#f3eee6;
    --haze:#e9dcc4;
    --meadow:#d8bf8e;
    --parchment:#dcc79f;
    --parchment-dark:#cfb687;
    --ink:#2b2520;
    --ink-soft:#3a322b;
    --ribbon:#a4581d;
    --ribbon-dark:#7a3a12;
    --frame:#8b3222;
    --recycle:#b4551b;
  }
  *{margin:0;padding:0;box-sizing:border-box}
  html,body{width:1200px;height:1200px;overflow:hidden;background:var(--page)}
  .canvas{position:relative;width:1200px;height:1200px}
  .pack{
    position:absolute;left:304px;top:122px;width:570px;height:922px;overflow:hidden;
    background:linear-gradient(180deg,var(--parchment) 0%,#d9c399 55%,var(--parchment-dark) 100%);
    font-family:"PT Sans",sans-serif;color:var(--ink);
  }
  .hero{
    position:absolute;left:0;top:0;width:570px;height:380px;
    background:
      radial-gradient(ellipse 80px 90px at 212px 270px,rgba(140,70,30,.8),rgba(140,70,30,0) 100%),
      linear-gradient(180deg,var(--sky) 0%,#f4efe7 35%,var(--haze) 62%,var(--meadow) 85%,rgba(216,191,142,0) 100%);
  }
  .hang-slot{position:absolute;left:208px;top:15px}
  .headline{
    position:absolute;left:0;width:570px;top:102px;text-align:center;
    font-family:"Black Ops One",sans-serif;font-weight:400;font-size:22px;font-variant:small-caps;
    letter-spacing:.5px;color:#1f1a16;
  }
  .story-side{position:absolute;left:321px;width:204px;font-size:12.5px;line-height:14.6px;color:var(--ink-soft)}
  .story-side.first{top:142px}
  .story-side.second{top:229px}
  .story-wide{position:absolute;left:25px;width:508px;font-size:12.5px;line-height:14.6px;color:var(--ink-soft)}
  .story-wide.p1{top:371px}
  .story-wide.p2{top:422px}
  .story-wide.p3{top:472px}
  .ribbon{position:absolute;left:25px;top:547px}
  .ribbon-title{
    position:absolute;left:25px;top:547px;width:511px;height:38px;line-height:40px;text-align:center;
    font-family:"Black Ops One",sans-serif;font-weight:400;font-size:21px;font-variant:small-caps;color:#fbf4e6;
  }
  .ingredients,.storage{
    position:absolute;left:35px;width:232px;font-family:"PT Sans Narrow",sans-serif;
    font-size:13px;line-height:17.4px;color:var(--ink-soft);
  }
  .ingredients{top:606px}
  .storage{top:676px}
  .nutrition{
    position:absolute;left:344px;top:610px;width:191px;height:188px;border:1px solid var(--frame);
    font-family:"PT Sans Narrow",sans-serif;font-size:13px;line-height:14.6px;color:var(--ink-soft);
  }
  .nutrition-head{padding:4px 6px;height:40px;border-bottom:1px solid var(--frame)}
  .nutrition-rows{padding:7px 14px 0 10px}
  .row{display:flex;justify-content:space-between}
  .recycle{position:absolute;left:31px;top:791px}
</style>
</head>
<body>
<div class="canvas">
  <section class="pack">
    <div class="hero" role="img" aria-label="Foto: Bison in goldener Prärie vor den schneebedeckten Rocky Mountains"></div>

    <svg class="hang-slot" width="162" height="48" viewBox="0 0 162 48" aria-hidden="true">
      <path d="M20 25 H67 A19 19 0 0 1 105 25 H150 A12 12 0 0 1 150 48 H20 A12 12 0 0 1 20 25 Z" fill="#ffffff" opacity=".92"/>
    </svg>

    <h1 class="headline">Das zeichnet unsere Bisons aus</h1>

    <p class="story-side first">Unsere Bisons grasen ganzjährig auf ihren ursprünglichen Weidegrün-den Nordamerikas zu Füßen der Rocky Mountains im Bundeststaat Alberta.</p>
    <p class="story-side second">Bis zur Schlachtreife von ca. drei Jahren weiden die Bisons so in ihrem natürlichen Habitat. Dies un-terscheidet den Bison deutlich vom Rind, welches normalerweise be-reits vor seinem zweiten Lebensjahr geschlachtet wird.</p>

    <p class="story-wide p1">Eine große Nahrungsvielfalt und ein behutsames langes Aufwachsen in seinem natürlichen Lebensraum sind der Grundstein für die außerordentliche Gesundheit der Tiere, die hohe Fleischqualität des Bisonfleisches und seinen besonders würzigen Geschmack.</p>
    <p class="story-wide p2">Bisonfleisch ist daher besonders reich an wichtigen Spurenelementen wie Eisen, Zink, Selen und ist vergleichsweise arm an Fett oder Cholesterin und eignet sich so besonders für eine gesundheitsbewusste Ernährung.</p>
    <p class="story-wide p3">Aufgrund ihrer geringen Anfälligkeit gegen Krankheiten benötigen Bisons im Gegensatz zum Rind keine Futterergänzungsmittel, Präparate wie Hormone oder andere Medikamente wie Antibiotika.</p>

    <svg class="ribbon" width="511" height="38" viewBox="0 0 511 38" aria-hidden="true">
      <path d="M0 0 H511 L495 19 L511 38 H0 L16 19 Z" fill="var(--ribbon)" stroke="var(--ribbon-dark)" stroke-width="1"/>
    </svg>
    <h2 class="ribbon-title">Der perfekte Snack</h2>

    <p class="ingredients">Zutaten: Bisonfleisch | Gewürzextrakte | Salz | Gewürze | Würze | Antioxidationsmittel | Ascorbin-säure | Natriumnitrit | Raucaroma</p>
    <p class="storage">Kann Spuren von Nüsen enthalten. Trocken und kühl bei 4 - max. 30° lagern. Nach dem Öffnen im Kühl-schrank aufbewahren und innerhalb von 4 - 5 Tagen verbrauchen.</p>

    <div class="nutrition">
      <div class="nutrition-head">Durchschnittliche<br>Nährwerte&nbsp; pro 100 g</div>
      <div class="nutrition-rows">
        <div class="row"><span>Energie</span><span>1194 kJ</span></div>
        <div class="row"><span></span><span>282 kcal</span></div>
        <div class="row"><span>Fett</span><span>3,4 g</span></div>
        <div class="row"><span>davon gesättigte</span><span></span></div>
        <div class="row"><span>Fettsäuren</span><span>2,2 g</span></div>
        <div class="row"><span>Kohlenhydrate</span><span>14,8 g</span></div>
        <div class="row"><span>davon Zucker</span><span>12,7 g</span></div>
        <div class="row"><span>Eiweiß</span><span>48 g</span></div>
        <div class="row"><span>Salz</span><span>3,7 g</span></div>
      </div>
    </div>

    <svg class="recycle" width="78" height="74" viewBox="0 0 78 74" role="img" aria-label="Recycling-Symbol">
      <g fill="var(--recycle)">
        <path d="M30 4 H48 L58 20 L65 16 L60 34 L43 30 L50 26 L42 12 L34 26 L22 19 Z"/>
        <path d="M70 40 L78 56 L68 70 H50 V78 L40 64 L50 50 V58 H64 L58 46 Z" transform="translate(0,-6)"/>
        <path d="M8 36 L20 30 L28 44 L34 44 L28 60 L14 50 L21 50 L16 42 L10 54 H32 V68 H10 L0 52 Z"/>
      </g>
    </svg>
  </section>
</div>
</body>
</html>
```